Rack Card Design for an Ayurvedic Beauty Product Project

Hello, I need to have rack cards. The rack cards would be about 3 products we are showcasing at an event. I am a cosmetic company. I have a logo and basic design ideas. I have attached some product images and info. By no means am I a designer so please excuse my messy AI files. Please feel free to design this as feminine as you like. :)

Target Market(s)

Beauty industry, organic, holistic, ayurveda

Industry/Entity Type

Cosmetic

```html
<!DOCTYPE html>
<html lang="en">
<head>
<meta charset="utf-8">
<title>Amber Petal Rack Cards</title>
<link href="https://fonts.googleapis.com/css2?family=Jost:wght@300;400;600&display=swap" rel="stylesheet">
<style>
  :root {
    --backdrop: #946c41;
    --plum: #84205f;
    --plum-deep: #5b1143;
    --plum-text: #7b1b5c;
    --gold-light: #d4b072;
    --gold: #c29a5c;
    --gold-deep: #a9834b;
    --white: #ffffff;
  }
  * { margin: 0; padding: 0; box-sizing: border-box; }
  html, body {
    width: 1200px; height: 1145px; overflow: hidden;
    background: var(--backdrop);
    font-family: "Jost", sans-serif;
  }
  .canvas { position: relative; width: 1200px; height: 1145px; }

  .rack-card {
    position: absolute; top: 100px; width: 413px; height: 931px;
    background: linear-gradient(180deg, var(--plum) 0%, var(--plum-deep) 100%);
    box-shadow: 0 6px 14px rgba(0,0,0,0.35);
    overflow: hidden;
  }
  .rack-card--intro { left: 151px; }
  .rack-card--products { left: 615px; }

  .card-bands { position: absolute; inset: 0; width: 100%; height: 100%; }

  /* Intro card */
  .intro-frame {
    position: absolute; left: 12px; top: 12px; right: 12px; bottom: 12px;
    border: 3px solid var(--gold);
  }
  .brand-dot {
    position: absolute; left: 50%; top: 58px; width: 118px; height: 118px;
    margin-left: -59px; border-radius: 50%;
    background: linear-gradient(160deg, var(--gold-light), var(--gold-deep));
  }
  .brand-name {
    position: absolute; left: 0; right: 0; top: 238px;
    text-align: center; font-weight: 600; font-size: 28px; letter-spacing: 0.5px;
    color: var(--gold);
  }
  .intro-title {
    position: absolute; left: 0; right: 0; top: 278px;
    text-align: center; font-weight: 300; font-size: 27px; line-height: 31px;
    color: var(--white);
  }
  .intro-copy {
    position: absolute; left: 38px; right: 38px; top: 445px;
    text-align: center; font-weight: 400; font-size: 21px; line-height: 26px;
    color: var(--plum-text);
  }

  /* Product card */
  .product { position: absolute; text-align: center; color: var(--white); }
  .product-name { font-weight: 600; font-size: 18px; line-height: 22px; margin-bottom: 8px; }
  .product-copy { font-weight: 300; font-size: 18px; line-height: 22px; }
  .product--toner { left: 30px; width: 230px; top: 39px; }
  .product--cream { left: 168px; width: 220px; top: 327px; }
  .product--serum { left: 30px; width: 248px; top: 606px; }

  .product-shot { position: absolute; }
  .product-shot--toner {
    left: 278px; top: 34px; width: 96px; height: 250px;
    border-radius: 8px 8px 14px 14px;
    background: linear-gradient(90deg, #6e1650, #9a3478 55%, #6a1249);
  }
  .product-shot--cream {
    left: 34px; top: 340px; width: 120px; height: 176px; border-radius: 12px;
    background: linear-gradient(90deg, #dcdcdc, #f7f7f7 50%, #d4d4d4);
  }
  .product-shot--serum {
    left: 286px; top: 602px; width: 86px; height: 272px;
    border-radius: 6px 6px 14px 14px;
    background: linear-gradient(90deg, #6e1650, #9a3478 55%, #6a1249);
  }
</style>
</head>
<body>
<main class="canvas">

  <section class="rack-card rack-card--intro">
    <svg class="card-bands" viewBox="0 0 413 931" preserveAspectRatio="none" aria-hidden="true">
      <defs>
        <linearGradient id="introGold" x1="0" y1="0" x2="0" y2="1">
          <stop offset="0" stop-color="#d4b072"/>
          <stop offset="1" stop-color="#b38b50"/>
        </linearGradient>
      </defs>
      <path d="M12 406 C90 425 150 420 220 398 C290 378 350 378 401 402 L401 919 L12 919 Z" fill="url(#introGold)"/>
    </svg>
    <div class="intro-frame"></div>
    <div class="brand-dot"></div>
    <h1 class="brand-name">AMBER PETAL</h1>
    <h2 class="intro-title">Ayurvedic<br>Firming &amp; Lifting<br>Breast Cream</h2>
    <p class="intro-copy">Amber Petal curates organic infused products where holistic skin care meets a luxurious experience. Each ingredient is carefully selected; providing Ayurvedic herbs, rich minerals &amp; elements. Stimulating hydration and anti-oxidants to lift, firm and illuminate your skin. We believe in connecting with your inner mantra, stimulating higher vibrations, self-esteem, positive mind and soul. As a brand we work with our experts/suppliers of Ayurveda to ensure that our products meet the quality, wholesome healing that you need.</p>
  </section>

  <section class="rack-card rack-card--products">
    <svg class="card-bands" viewBox="0 0 413 931" preserveAspectRatio="none" aria-hidden="true">
      <defs>
        <linearGradient id="bandGold" x1="0" y1="0" x2="0" y2="1">
          <stop offset="0" stop-color="#d4b072"/>
          <stop offset="1" stop-color="#a9834b"/>
        </linearGradient>
      </defs>
      <path d="M12 288 C90 300 170 300 250 272 C310 252 360 250 401 258 L401 540 C340 530 280 545 210 565 C140 585 70 590 12 582 Z" fill="url(#bandGold)"/>
    </svg>

    <div class="product product--toner">
      <h3 class="product-name">Amber Petal Firming &amp;<br>Lifting Breast Toner</h3>
      <p class="product-copy">Using all natural Ayurvedic herbs, our breast toner, prepares the area for maximum absorption, giving you the best results and the most invigorating treatment</p>
    </div>
    <div class="product-shot product-shot--toner" role="img" aria-label="Product photo of the breast toner in a plum squeeze tube with gold cap"></div>

    <div class="product-shot product-shot--cream" role="img" aria-label="Product photo of the breast cream in a white jar with gold lid"></div>
    <div class="product product--cream">
      <h3 class="product-name">Amber Petal Firming &amp;<br>Lifting Breast Cream</h3>
      <p class="product-copy">Using all natural Ayurvedic herbs, our breast cream helps enhance, tighten, and lift your breast</p>
    </div>

    <div class="product product--serum">
      <h3 class="product-name">Amber Petal Firming and<br>Toning Breast Serum</h3>
      <p class="product-copy">Using all natural Ayurvedic herbs, and a touch of 24k gold, our serum enhances the experience and quality of results when partnered with the Amber Petal Firming and Lifting Breast Cream providing an all-dayboosting experience</p>
    </div>
    <div class="product-shot product-shot--serum" role="img" aria-label="Product photo of the breast serum in a plum tube with gold cap"></div>
  </section>

</main>
</body>
</html>
```